Marn-ridge Tide Harbor Custom Brokers Limited

Name: Dorvella Hastings
Title: Customs Broker
Address: Shop 9 Birchfield Commercial Complex
207-209 Harlow Road
Kingston 8
Telephone: (876)
Email: tideharborport@quillmail.example

```html
<!DOCTYPE html>
<html lang="en">
<head>
<meta charset="utf-8">
<title>Marn-ridge Tide Harbor Custom Brokers Limited – Business Card</title>
<link rel="stylesheet" href="https://fonts.googleapis.com/css2?family=Poppins:wght@400;500;600;700&display=swap">
<style>
  :root {
    --navy: #142d55;
    --gold: #e9ab22;
    --white: #ffffff;
    --grey: #8a8f98;
    --globe: #d9dbdf;
    --backdrop: #2a2a2b;
  }
  * { box-sizing: border-box; margin: 0; padding: 0; }
  html, body {
    width: 1200px; height: 900px; overflow: hidden;
    background: var(--backdrop);
    font-family: "Poppins", sans-serif;
  }
  .sheet {
    width: 1200px; height: 900px;
    display: flex; flex-direction: column; align-items: center; justify-content: center;
    gap: 30px;
  }
  .card {
    position: relative;
    width: 720px; height: 410px;
    border-radius: 22px;
    overflow: hidden;
  }
  /* Back side */
  .card--back { background: var(--navy); display: flex; align-items: center; justify-content: center; }
  .brand { display: flex; align-items: center; gap: 16px; }
  .brand__dot { width: 46px; height: 46px; border-radius: 50%; flex: none; }
  .brand__name { font-weight: 600; line-height: 1.2; letter-spacing: 0.02em; }
  .card--back .brand__dot { background: var(--gold); }
  .card--back .brand__name { color: var(--white); font-size: 25px; }

  /* Front side */
  .card--front { background: var(--white); }
  .front__globe {
    position: absolute; right: 20px; top: 0;
    width: 330px; height: 175px;
    border-radius: 0 0 165px 165px;
    background: radial-gradient(ellipse at 50% 20%, #f4f5f7 0%, var(--globe) 100%);
  }
  .front__brand { position: absolute; left: 48px; top: 130px; }
  .card--front .brand__dot { background: var(--navy); }
  .card--front .brand__name { color: var(--navy); font-size: 21px; }

  .person { position: absolute; right: 46px; top: 180px; text-align: right; }
  .person__name { color: var(--navy); font-weight: 700; font-size: 24px; letter-spacing: 0.02em; text-transform: uppercase; }
  .person__title { color: var(--gold); font-weight: 500; font-size: 16px; letter-spacing: 0.03em; text-transform: uppercase; margin-top: -2px; }
  .person__rule { height: 1.5px; background: var(--navy); width: 300px; margin: 8px 0 0 auto; }

  .address {
    position: absolute; right: 46px; top: 258px;
    display: flex; gap: 10px; align-items: flex-start;
    color: var(--navy); font-size: 15px; line-height: 1.45; text-align: right;
  }
  .address__icon { width: 16px; height: 20px; margin-top: 2px; order: 2; flex: none; }

  .divider { position: absolute; left: 48px; top: 300px; width: 280px; height: 1.5px; background: var(--navy); }

  .contact { position: absolute; left: 48px; top: 312px; list-style: none; color: var(--navy); font-size: 15px; }
  .contact li { display: flex; align-items: center; gap: 12px; line-height: 1.6; }
  .contact svg { width: 18px; height: 18px; flex: none; }

  .bands { position: absolute; left: 0; bottom: 0; width: 720px; height: 70px; }
</style>
</head>
<body>
<main class="sheet">

  <section class="card card--back" aria-label="Card back">
    <div class="brand">
      <span class="brand__dot"></span>
      <p class="brand__name">Marn-ridge Tide Harbor<br>Custom Brokers Limited</p>
    </div>
  </section>

  <section class="card card--front" aria-label="Card front">
    <div class="front__globe" role="img" aria-label="Grey line drawing of a globe"></div>

    <div class="brand front__brand">
      <span class="brand__dot"></span>
      <p class="brand__name">Marn-ridge Tide Harbor<br>Custom Brokers Limited</p>
    </div>

    <div class="person">
      <h1 class="person__name">Dorvella Hastings</h1>
      <p class="person__title">Customs Broker</p>
      <div class="person__rule"></div>
    </div>

    <div class="address">
      <svg class="address__icon" viewBox="0 0 16 20" aria-hidden="true">
        <path d="M8 1a6 6 0 0 0-6 6c0 4.5 6 11.5 6 11.5S14 11.5 14 7a6 6 0 0 0-6-6z" fill="none" stroke="var(--gold)" stroke-width="2"/>
        <circle cx="8" cy="7" r="2.2" fill="var(--gold)"/>
      </svg>
      <p>Shop 9 Birchfield Commercial Complex<br>207-209 Harlow Road<br>Kingston 8</p>
    </div>

    <div class="divider"></div>

    <ul class="contact">
      <li>
        <svg viewBox="0 0 24 24" aria-hidden="true"><path d="M6.6 10.8a15 15 0 0 0 6.6 6.6l2.2-2.2a1 1 0 0 1 1-.25 11.4 11.4 0 0 0 3.6.57 1 1 0 0 1 1 1V20a1 1 0 0 1-1 1A17 17 0 0 1 3 4a1 1 0 0 1 1-1h3.5a1 1 0 0 1 1 1c0 1.25.2 2.45.57 3.6a1 1 0 0 1-.25 1z" fill="var(--gold)"/></svg>
        (876) 555-014-2290
      </li>
      <li>
        <svg viewBox="0 0 24 24" aria-hidden="true"><rect x="2" y="5" width="20" height="14" fill="var(--gold)"/><path d="M2 5l10 8 10-8" fill="none" stroke="var(--white)" stroke-width="1.6"/></svg>
        tideharborport@quillmail.example
      </li>
    </ul>

    <svg class="bands" viewBox="0 0 720 70" aria-hidden="true">
      <polygon points="0,48 470,34 458,70 0,70" fill="var(--navy)"/>
      <polygon points="478,33 490,33 478,70 466,70" fill="var(--gold)"/>
      <polygon points="496,32 720,24 720,70 484,70" fill="var(--gold)"/>
    </svg>
  </section>

</main>
</body>
</html>
```